Design for a 4 screens mobile app: Brightnook

The app is a compact but illustrated phone/address book...
We need a design for the 5 screens of the app (see screens attached):
a) "index" : 1 screen with 6 pictures of contact person
b) "contact list" : 1 screen, to manage (add/del/edit) the contacts of the phone/address book
c) "add contact" : 1 screen to add a contact (a picture + a phone number)
d) "update contact" : similar to "add"
e) "fields missing" : add/edit screens in "error" state
We also need the ico design + loading screen.
No specific guidelines, nor logo or whatever.
It will be a free app distributed on iOS and Androïd.
We just want to make it looking nice & very usable for end users.
B2C

```html
<!DOCTYPE html>
<html lang="en">
<head>
<meta charset="utf-8">
<title>Brightnook – Update Contact</title>
<link href="https://fonts.googleapis.com/css2?family=Quicksand:wght@400;500;600&display=swap" rel="stylesheet">
<style>
  :root {
    --page-bg: #e6e6e6;
    --coral: #f47274;
    --screen-bg: #f1f1f1;
    --white: #ffffff;
    --photo-dark: #2a2422;
    --photo-mid: #8a7a6c;
    --photo-light: #cfc6b8;
    --green: #5cbf45;
  }
  * { box-sizing: border-box; margin: 0; padding: 0; }
  html, body {
    width: 1200px; height: 1139px; overflow: hidden;
    background: var(--page-bg);
    font-family: "Quicksand", sans-serif;
  }
  .screen {
    position: absolute; left: 290px; top: 20px;
    width: 620px; height: 1099px;
    background: var(--screen-bg);
    overflow: hidden;
  }
  .app-bar {
    background: var(--coral); color: var(--white);
    height: 128px; position: relative;
  }
  .status-bar {
    height: 44px; display: flex; align-items: center; justify-content: space-between;
    padding: 0 18px; font-size: 15px; font-weight: 600;
  }
  .status-left, .status-right { display: flex; align-items: center; gap: 6px; width: 160px; }
  .status-right { justify-content: flex-end; }
  .status-time { font-weight: 600; }
  .nav-row {
    height: 84px; display: flex; align-items: center; justify-content: space-between;
    padding: 0 22px;
  }
  .screen-title { font-size: 24px; font-weight: 400; letter-spacing: 0.5px; }
  .nav-button { width: 32px; height: 32px; display: block; }
  .contact-photo {
    height: 440px;
    background: linear-gradient(160deg, var(--photo-light) 0%, var(--photo-mid) 35%, var(--photo-dark) 60%, var(--photo-mid) 100%);
  }
  .contact-actions { position: relative; height: 527px; }
  .phone-number {
    position: absolute; left: 130px; top: 90px;
    width: 300px; height: 66px; border-radius: 6px;
    background: var(--coral); color: var(--white);
    font-size: 27px; font-weight: 500; letter-spacing: 0.5px;
    display: flex; align-items: center; justify-content: center;
  }
  .pick-photo { position: absolute; left: 470px; top: 86px; width: 74px; height: 70px; }
  .delete-contact { position: absolute; left: 232px; top: 220px; width: 76px; height: 76px; }
</style>
</head>
<body>
  <main class="screen">
    <header class="app-bar">
      <div class="status-bar">
        <div class="status-left">
          <svg width="26" height="12" viewBox="0 0 26 12" fill="#fff"><rect x="0" y="8" width="3" height="4"/><rect x="5" y="6" width="3" height="6"/><rect x="10" y="4" width="3" height="8"/><rect x="15" y="2" width="3" height="10"/><rect x="20" y="0" width="3" height="12"/></svg>
          <span>NET</span>
          <svg width="18" height="14" viewBox="0 0 18 14" fill="none" stroke="#fff" stroke-width="2"><path d="M1 5a12 12 0 0 1 16 0"/><path d="M4 8.5a7 7 0 0 1 10 0"/><circle cx="9" cy="12" r="1.2" fill="#fff"/></svg>
        </div>
        <span class="status-time">2:52 PM</span>
        <div class="status-right">
          <svg width="16" height="16" viewBox="0 0 16 16" fill="none" stroke="#fff" stroke-width="2"><circle cx="8" cy="8" r="6"/><path d="M8 4v4l3 2"/></svg>
          <span>53 %</span>
          <svg width="28" height="14" viewBox="0 0 28 14" fill="none" stroke="#fff" stroke-width="1.5"><rect x="1" y="1" width="23" height="12" rx="2"/><rect x="3" y="3" width="11" height="8" fill="#fff" stroke="none"/><path d="M26 5v4"/></svg>
        </div>
      </div>
      <nav class="nav-row">
        <svg class="nav-button" viewBox="0 0 32 32" fill="none" stroke="#fff" stroke-width="4" stroke-linecap="round" stroke-linejoin="round" aria-label="Back"><path d="M12 6 5 13l7 7"/><path d="M6 13h12a8 8 0 0 1 8 8v5"/></svg>
        <h1 class="screen-title">Update Contact</h1>
        <svg class="nav-button" viewBox="0 0 32 32" aria-label="Save"><circle cx="16" cy="16" r="14" fill="#fff"/><path d="M9 16.5l5 5 9-10" fill="none" stroke="var(--coral)" stroke-width="3.5" stroke-linecap="round" stroke-linejoin="round"/></svg>
      </nav>
    </header>

    <div class="contact-photo" role="img" aria-label="Contact photo: selfie of a person with long dark hair in a grey top"></div>

    <section class="contact-actions">
      <div class="phone-number">(1) 55 0123 4567</div>

      <svg class="pick-photo" viewBox="0 0 74 70" aria-label="Choose photo">
        <g fill="var(--green)">
          <rect x="22" y="22" width="46" height="38" rx="2" transform="rotate(12 45 41)"/>
          <rect x="14" y="16" width="46" height="38" rx="2" transform="rotate(6 37 35)" stroke="var(--screen-bg)" stroke-width="3"/>
          <rect x="6" y="10" width="46" height="38" rx="2" stroke="var(--screen-bg)" stroke-width="3"/>
        </g>
        <rect x="12" y="16" width="34" height="26" fill="var(--screen-bg)"/>
        <circle cx="29" cy="25" r="5" fill="var(--green)"/>
        <path d="M18 42c0-8 5-11 11-11s11 3 11 11z" fill="var(--green)"/>
      </svg>

      <svg class="delete-contact" viewBox="0 0 76 76" aria-label="Delete contact">
        <g fill="var(--coral)">
          <path d="M4 20c8-10 18-12 26-6l-4 3 10 3-1-10-3 3C23 6 11 9 4 20z"/>
          <rect x="22" y="24" width="44" height="6" rx="2" transform="rotate(-10 44 27)"/>
          <path d="M24 34h40l-4 38H28z"/>
        </g>
        <g stroke="var(--screen-bg)" stroke-width="3" stroke-linecap="round">
          <path d="M36 42v22M44 42v22M52 42v22"/>
        </g>
      </svg>
    </section>
  </main>
</body>
</html>
```